Blueprints For A Steady Home Book*

Our book is about using engineering and biblical principles to solve problems in marriage. We are the wedlock Architects. See our branded logo in the attachments. We would like to see different types of graphics that shows continuous improvement in marriage. Our colors should be Gold Black and Red. Could use white text and symbols if needed. Brief description on the back with some quotes and our Picture. Use 5.5x8.5 as the size of the book. Not sure about the spine size.

Target Market(s)

Married couples

Font styles to use
Serif

Colors

Designer to choose colors to be used in the design.

Requirements
Nice to have
• Engineering symbols and Logos.

```html
<!DOCTYPE html>
<html lang="en">
<head>
<meta charset="utf-8">
<title>Blueprints For A Steady Home – Cover Spread</title>
<link href="https://fonts.googleapis.com/css2?family=Oswald:wght@500;700&family=Great+Vibes&family=Roboto+Condensed:wght@400&display=swap" rel="stylesheet">
<style>
  :root {
    --page-bg: #eeeeee;
    --cover-dark: #242424;
    --cover-mid: #383838;
    --spine-dark: #1f1f1f;
    --gold: #d6aa3a;
    --white: #ffffff;
    --chalk: rgba(255,255,255,0.22);
    --red: #c3262b;
  }
  * { box-sizing: border-box; margin: 0; padding: 0; }
  html, body { width: 900px; height: 1200px; overflow: hidden; }
  body { background: var(--page-bg); position: relative; }

  .cover-spread {
    position: absolute;
    left: 10px; top: 283px;
    width: 880px; height: 634px;
    display: flex;
    box-shadow: 0 2px 8px rgba(0,0,0,0.25);
  }
  .back-cover, .front-cover, .spine {
    position: relative;
    height: 100%;
    overflow: hidden;
  }
  .back-cover { width: 415px; }
  .spine { width: 50px; background: var(--spine-dark); }
  .front-cover { width: 415px; }

  .chalk-backdrop {
    position: absolute; inset: 0;
    background: radial-gradient(ellipse at 50% 50%, var(--cover-mid) 0%, var(--cover-dark) 78%);
  }
  .chalk-graphs {
    position: absolute; inset: 0;
    width: 100%; height: 100%;
  }
  .chalk-graphs path, .chalk-graphs line, .chalk-graphs polyline {
    fill: none; stroke: var(--chalk); stroke-width: 1.4; stroke-linecap: round;
  }

  .blurb {
    position: absolute;
    left: 30px; top: 34px; width: 350px;
    font-family: "Roboto Condensed", sans-serif;
    font-size: 9.5px;
    line-height: 1.6;
    letter-spacing: 0.3px;
    text-transform: uppercase;
    color: var(--white);
  }
  .blurb p + p { margin-top: 14px; }

  .title-block {
    position: absolute;
    left: 0; right: 0; top: 60px;
    text-align: center;
  }
  .title-main {
    font-family: "Oswald", sans-serif;
    font-weight: 700;
    font-size: 52px;
    letter-spacing: 1px;
    color: var(--gold);
    line-height: 1;
  }
  .title-sub {
    font-family: "Great Vibes", cursive;
    font-size: 32px;
    color: var(--white);
    line-height: 1.1;
    margin-top: 2px;
  }

  .couple-art {
    position: absolute;
    left: 50%; top: 170px;
    width: 330px; height: 300px;
    transform: translateX(-50%);
    border-radius: 50%;
    background: radial-gradient(ellipse at 50% 55%, rgba(195,38,43,0.55) 0%, rgba(247,230,230,0.75) 38%, rgba(255,255,255,0.0) 70%);
  }

  .brand-mark {
    position: absolute;
    left: 0; right: 0; bottom: 26px;
    display: flex; flex-direction: column; align-items: center; gap: 6px;
  }
  .brand-dot {
    width: 20px; height: 20px; border-radius: 50%;
    background: var(--gold);
  }
  .brand-name {
    font-family: "Oswald", sans-serif;
    font-weight: 500;
    font-size: 12px;
    letter-spacing: 1.5px;
    text-transform: uppercase;
    color: var(--gold);
  }

  .spine-title {
    position: absolute;
    left: 50%; top: 36px;
    transform: translateX(-50%);
    writing-mode: vertical-rl;
    white-space: nowrap;
    display: flex; align-items: center; gap: 8px;
  }
  .spine-main {
    font-family: "Oswald", sans-serif;
    font-weight: 700;
    font-size: 24px;
    color: var(--gold);
    letter-spacing: 1px;
  }
  .spine-sub {
    font-family: "Great Vibes", cursive;
    font-size: 19px;
    color: var(--white);
  }
  .spine-mark {
    position: absolute;
    left: 50%; bottom: 26px;
    transform: translateX(-50%);
    width: 16px; height: 16px; border-radius: 50%;
    background: var(--gold);
  }
</style>
</head>
<body>
  <section class="cover-spread">
    <div class="back-cover">
      <div class="chalk-backdrop" role="img" aria-label="Dark chalkboard covered in faint hand-written equations and graphs"></div>
      <svg class="chalk-graphs" viewBox="0 0 415 634" aria-hidden="true">
        <line x1="40" y1="590" x2="190" y2="590"/>
        <line x1="40" y1="590" x2="40" y2="450"/>
        <polyline points="40,575 70,560 100,548 130,520 160,498 188,462"/>
        <line x1="240" y1="590" x2="390" y2="590"/>
        <line x1="240" y1="590" x2="240" y2="450"/>
        <path d="M250 470 Q310 600 380 470"/>
        <path d="M60 330 Q130 260 200 330 T340 330"/>
      </svg>
      <div class="blurb">
        <p>Every marriage is a structure that needs a sound design, honest measurements and steady upkeep. This book shows couples how to apply careful engineering thinking and timeless biblical wisdom to the everyday problems of shared life, so that small cracks are found early and repaired with patience, grace and a clear plan.</p>
        <p>Inside you will find simple tools for listening, planning and testing new habits together. Each chapter builds on the last, guiding husband and wife toward a home that grows stronger and more joyful with every passing season of their life together.</p>
      </div>
    </div>

    <div class="spine">
      <div class="spine-title">
        <span class="spine-main">BLUEPRINTS</span>
        <span class="spine-sub">For A Steady Home</span>
      </div>
      <div class="spine-mark"></div>
    </div>

    <div class="front-cover">
      <div class="chalk-backdrop" role="img" aria-label="Dark chalkboard covered in faint hand-written equations and graphs"></div>
      <svg class="chalk-graphs" viewBox="0 0 415 634" aria-hidden="true">
        <line x1="24" y1="600" x2="150" y2="600"/>
        <line x1="24" y1="600" x2="24" y2="480"/>
        <polyline points="24,590 50,575 76,560 102,532 128,510 148,486"/>
        <line x1="280" y1="600" x2="395" y2="600"/>
        <line x1="280" y1="600" x2="280" y2="480"/>
        <path d="M285 590 Q340 590 390 490"/>
        <path d="M20 170 Q45 140 70 170 T120 170"/>
        <path d="M300 160 Q345 120 395 160"/>
      </svg>
      <div class="title-block">
        <h1 class="title-main">BLUEPRINTS</h1>
        <div class="title-sub">For A Steady Home</div>
      </div>
      <div class="couple-art" role="img" aria-label="Heart-framed illustration of a couple sitting on two swings"></div>
      <div class="brand-mark">
        <div class="brand-dot"></div>
        <div class="brand-name">the wedlock Architects</div>
      </div>
    </div>
  </section>
</body>
</html>
```